Brovatik Support Services Brochure and Flyer

I need a brochure and DL flyer created for a business that provides staff to people who live with disability and mental health. The wording is available, just looking for some clean designs with images that show natural people. I am also looking for something professional and catchy.

```html
<!DOCTYPE html>
<html lang="en">
<head>
<meta charset="utf-8">
<title>Brovatik Support Services – DL Flyer</title>
<link href="https://fonts.googleapis.com/css2?family=Overpass:wght@400;500;600;700;800&display=swap" rel="stylesheet">
<style>
  :root{
    --sky:#1a9ad6;
    --royal:#1047b0;
    --royal-light:#2a6fd0;
    --orange:#f7941d;
    --ink:#2e2e2e;
    --paper:#ffffff;
    --backdrop:#4b4e53;
  }
  *{margin:0;padding:0;box-sizing:border-box}
  html,body{width:1200px;height:1200px;overflow:hidden}
  body{background:var(--backdrop);font-family:"Overpass",Arial,sans-serif;color:var(--ink);position:relative}
  .panel{position:absolute;top:80px;width:507px;height:1020px;background:var(--paper);overflow:hidden}
  .panel--front{left:72px}
  .panel--back{left:619px}
  .abs{position:absolute}
  .shape{position:absolute;left:0;top:0}
  p,li{font-size:13.4px;line-height:16.4px}
  .justify{text-align:justify}

  /* front */
  .brand{position:absolute;display:flex;align-items:center;gap:8px;color:var(--royal);font-weight:600;font-size:20px;line-height:22px}
  .brand__dot{width:26px;height:26px;border-radius:50%;background:var(--orange);flex:none}
  .front__brand{left:262px;top:22px;width:230px}
  .tag{left:0;top:76px;width:146px;height:30px;background:var(--orange);border-radius:0 15px 15px 0;color:#fff;font-weight:700;font-size:20px;line-height:32px;padding-left:26px}
  .about__text{left:29px;top:113px;width:455px;color:#fff}
  .heading{font-size:19px;font-weight:600;color:var(--sky)}
  .heading .accent{color:var(--orange)}
  .why__title{left:23px;top:246px}
  .why__text{left:23px;top:272px;width:461px}
  .staff__title{left:23px;top:432px}
  .staff__text{left:23px;top:457px;width:461px}
  .requirements{left:23px;top:530px;width:470px;list-style:none}
  .requirements li,.supports li{position:relative;padding-left:14px;font-weight:500;color:#1d1d1d}
  .requirements li::before,.supports li::before{content:"";position:absolute;left:1px;top:6px;width:5px;height:5px;border-radius:50%;background:var(--orange)}
  .web-badge{left:438px;top:955px;width:40px;height:40px;border-radius:50%;background:var(--sky);border:3px solid #fff;display:flex;align-items:center;justify-content:center}
  .front__footer{left:0;top:980px;width:507px;height:40px;background:var(--orange);color:#fff;font-size:19px;text-align:center;line-height:44px}
  .front__footer b{font-weight:700}

  /* back */
  .back__brand{left:14px;top:36px;width:110px;font-size:17px}
  .provide__title{left:174px;top:16px;width:333px;height:32px;background:#fff;border-radius:16px 0 0 16px;color:var(--orange);font-weight:700;font-size:17px;line-height:35px;padding-left:24px}
  .service{position:absolute;left:134px;width:356px;display:flex;gap:12px}
  .service__icon{width:34px;height:34px;flex:none}
  .service p{color:#fff;text-align:justify;line-height:15.6px}
  .service b{font-weight:700}
  .specialised{left:30px;top:414px;font-size:24px;line-height:26px;font-weight:700;color:var(--sky)}
  .specialised .accent{color:var(--orange)}
  .specialised__rule{left:30px;top:510px;width:86px;height:4px;background:var(--orange);border-radius:2px;opacity:.8}
  .supports{left:18px;top:552px;width:470px;list-style:none}
  .supports li{font-weight:400}
  .supports b{color:var(--sky);font-weight:600}
  .closing{left:18px;top:823px;width:466px}
  .contact{right:30px;top:932px;text-align:right;color:#fff;font-size:13.6px;line-height:16.3px}
  .contact__row{display:flex;justify-content:flex-end;align-items:center;gap:6px}
  .contact__row b{font-weight:700}
  .contact-tab{left:0;top:976px;color:#fff;font-size:14px;font-weight:500;padding:14px 0 0 22px}
</style>
</head>
<body>

<!-- Front of flyer -->
<section class="panel panel--front">
  <svg class="shape" width="507" height="1020" viewBox="0 0 507 1020" aria-hidden="true">
    <path d="M0 0H507V180Q260 262 0 190Z" fill="var(--sky)"/>
    <path d="M235 0H507V88Q470 118 380 114Q240 108 228 48Q225 18 235 0Z" fill="#fff"/>
  </svg>
  <div class="brand front__brand"><span class="brand__dot"></span>Brovatik Support Services</div>

  <div class="abs tag">About Us</div>
  <p class="abs about__text justify">Brovatik Support Services is a Perth based staffing agency focusing on recruitment and placement of personnel in disability services, mental health, acute care, and social assistance. Our mission is to match remarkable people and create authentic lasting relationships.</p>

  <h2 class="abs heading why__title"><span class="accent">Why work</span> with us</h2>
  <p class="abs why__text justify">Our values based recruitment identifies candidates' skills, knowledge, values, and experience amongst other suitability checks. With <b>over 10 years' experience</b> in healthcare recruitment, our consultants are adept in contemporary recruitment practices, industry expectations, NDIS compliance which includes the NDIS Code of Conduct and Quality and Safeguards framework, as well as tailored methods of identifying suitable candidates. We believe in fostering long term relationships with people which enables meaningful bonds and lasting relationships.</p>

  <h2 class="abs heading staff__title"><span class="accent">Staff</span> we supply</h2>
  <p class="abs staff__text justify">We attract and employ disability support workers, mental health support workers, service coordinators, and corporate support staff. Our minimum experience, compliance and training requirements for all support workers include:</p>

  <ul class="abs requirements">
    <li>9 months experience in a similar role</li>
    <li>Current police clearance (acquired within the last 3 months)</li>
    <li>A Certificate III or IV in Community Services or Individual Support</li>
    <li>NDIS worker orientation module (Quality, Safety and You)</li>
    <li>Current manual handling</li>
    <li>Medication administration</li>
    <li>Proof of working rights</li>
    <li>2 employment references</li>
    <li>Other relevant skillsets which include PEG feeding, Dysphagia, Epilepsy management, Catheter care etc.</li>
  </ul>

  <svg class="shape" style="top:728px" width="507" height="256" viewBox="0 0 507 256" role="img" aria-label="Photo of a smiling young man in a wheelchair sharing a laugh with a female support worker">
    <defs>
      <linearGradient id="frontPhoto" x1="0" y1="0" x2="1" y2="1">
        <stop offset="0" stop-color="#c9b9a8"/>
        <stop offset=".45" stop-color="#9a8f8a"/>
        <stop offset="1" stop-color="#e3c7a2"/>
      </linearGradient>
    </defs>
    <rect width="507" height="256" fill="url(#frontPhoto)"/>
    <path d="M0 0H150Q60 40 0 150Z" fill="#fff"/>
    <path d="M230 0Q180 120 250 256H300Q240 130 290 0Z" fill="#fff" opacity=".85"/>
    <path d="M20 110Q60 230 180 256H20Z" fill="#fff" opacity=".55"/>
  </svg>

  <div class="abs web-badge">
    <svg width="20" height="20" viewBox="0 0 20 20" aria-hidden="true"><g fill="none" stroke="#fff" stroke-width="1.6"><circle cx="10" cy="10" r="8"/><ellipse cx="10" cy="10" rx="3.5" ry="8"/><path d="M2 10H18M3.5 6H16.5M3.5 14H16.5"/></g></svg>
  </div>
  <div class="abs front__footer">www.<b>brovatik</b>.com.au</div>
</section>

<!-- Back of flyer -->
<section class="panel panel--back">
  <svg class="shape" width="507" height="1020" viewBox="0 0 507 1020" aria-hidden="true">
    <path d="M0 0H507V372C420 395 250 375 150 320C90 288 40 240 0 200Z" fill="var(--royal)"/>
    <path d="M0 186C40 226 90 274 150 306C250 361 420 381 507 358V372C420 395 250 375 150 320C90 288 40 240 0 200Z" fill="var(--royal-light)"/>
    <path d="M0 0H118Q140 60 120 110Q90 175 0 178Z" fill="#fff"/>
    <path d="M118 0Q145 70 118 118Q85 180 0 182" fill="none" stroke="var(--royal-light)" stroke-width="5"/>
    <path d="M140 1020Q260 925 507 905V1020Z" fill="var(--royal)"/>
    <path d="M160 1020Q280 940 507 925V1020Z" fill="var(--sky)"/>
    <path d="M0 976H200L168 1020H0Z" fill="var(--orange)"/>
  </svg>

  <div class="brand back__brand"><span class="brand__dot"></span>Brovatik</div>
  <div class="abs provide__title">Our support workers provide:</div>

  <div class="service" style="top:60px">
    <svg class="service__icon" viewBox="0 0 34 34" aria-hidden="true"><g fill="none" stroke="#f7c06a" stroke-width="1.6"><rect x="5" y="14" width="24" height="15" rx="1"/><circle cx="12" cy="8" r="3"/><circle cx="22" cy="8" r="3"/><path d="M5 20H29M17 14V29"/></g></svg>
    <p><b>Assistance with daily life</b> such as end to end personal care, household cleaning and or light yard maintenance</p>
  </div>
  <div class="service" style="top:110px">
    <svg class="service__icon" viewBox="0 0 34 34" aria-hidden="true"><g fill="#f7a53a"><circle cx="17" cy="9" r="4"/><circle cx="8" cy="14" r="3.3"/><circle cx="26" cy="14" r="3.3"/><path d="M10 28Q10 17 17 16Q24 17 24 28Z"/><path d="M2 28Q2 20 8 19Q12 20 12 24V28Z"/><path d="M32 28Q32 20 26 19Q22 20 22 24V28Z"/></g></svg>
    <p><b>Assistance with social</b> and community participation such as community access, events, appointments, work etc</p>
  </div>
  <div class="service" style="top:160px">
    <svg class="service__icon" viewBox="0 0 34 34" aria-hidden="true"><g fill="none" stroke="#fff" stroke-width="1.6"><circle cx="15" cy="17" r="11"/><circle cx="15" cy="17" r="6"/><path d="M15 17L28 5"/></g><circle cx="24" cy="24" r="7" fill="var(--orange)"/><path d="M20.5 24l2.5 2.5 4.5-5" fill="none" stroke="#fff" stroke-width="1.8"/></svg>
    <p>Transport <b>linked to goals</b> such as seeking or accessing employment and other goals related activities</p>
  </div>
  <div class="service" style="top:210px">
    <svg class="service__icon" viewBox="0 0 34 34" aria-hidden="true"><g fill="none" stroke="#f7c06a" stroke-width="1.5"><rect x="9" y="6" width="16" height="24"/><rect x="3" y="15" width="6" height="15"/><rect x="25" y="15" width="6" height="15"/><path d="M13 11h2M19 11h2M13 16h2M19 16h2M13 21h2M19 21h2M15 30v-4h4v4"/></g></svg>
    <p><b>Capacity building support</b> which includes improved social and community participation, improved relationships, improved health and wellbeing, improved life choices, improved daily living skills etc</p>
  </div>

  <svg class="shape" style="left:212px;top:318px" width="270" height="250" viewBox="0 0 270 250" role="img" aria-label="Photos of families enjoying time outdoors with a young person using a wheelchair">
    <defs>
      <linearGradient id="backPhotoA" x1="0" y1="0" x2="1" y2="1"><stop offset="0" stop-color="#8d7f6d"/><stop offset="1" stop-color="#c7b8a3"/></linearGradient>
      <linearGradient id="backPhotoB" x1="0" y1="0" x2="1" y2="1"><stop offset="0" stop-color="#b89a74"/><stop offset="1" stop-color="#6f6658"/></linearGradient>
    </defs>
    <path d="M205 80Q255 60 258 120Q262 185 215 185Q192 170 200 120Z" fill="var(--orange)"/>
    <path d="M70 10Q150 -6 190 30Q232 70 220 120Q205 150 150 145Q90 140 68 100Q50 55 70 10Z" fill="url(#backPhotoA)"/>
    <path d="M10 120Q50 98 100 112Q128 130 122 190Q112 230 60 228Q12 226 5 190Q0 145 10 120Z" fill="url(#backPhotoB)"/>
  </svg>

  <h2 class="abs specialised">Specialised<br>supports<br><span class="accent">we provide<br>include:</span></h2>
  <div class="abs specialised__rule"></div>

  <ul class="abs supports">
    <li><b>Dysphagia:</b> for participants who have trouble eating, drinking, or swallowing daily.</li>
    <li><b>Respiratory:</b> for participants requiring help with their breathing and maintenance of their respiratory health, including any associated care, comfort, planning or supports</li>
    <li><b>Nutrition:</b> for participants requiring help with the way they eat or understanding the food they need.</li>
    <li><b>Diabetes:</b> for participants who have daily problems with how much sugar is in their blood.</li>
    <li><b>Continence:</b> for participants who need daily assistance with toileting (bladder and bowel).</li>
    <li><b>Wound &amp; Pressure Care:</b> for participants who need daily wound and pressure care (resulting from pressure wounds or swollen limbs).</li>
    <li><b>Epilepsy:</b> for participants who need daily help managing the way epilepsy affects the way their brain and nerves work</li>
    <li>Other support required from time to time</li>
  </ul>

  <p class="abs closing justify">We provide support services to people who live with a physical, intellectual, psychosocial, or neurological disability. With every placement, we provide a letter of confirmation to verify staff have the skills, knowledge, and training to meet the placement requirements.</p>

  <div class="abs contact">
    <div class="contact__row">(08) 6100 2741 <svg width="11" height="11" viewBox="0 0 12 12" aria-hidden="true"><path d="M2 1.5l2 0 1 2.5-1.2 1a6 6 0 0 0 3.2 3.2l1-1.2 2.5 1v2a1 1 0 0 1-1 1A9 9 0 0 1 1 2.5a1 1 0 0 1 1-1z" fill="#fff"/></svg></div>
    <div class="contact__row">Bookings@brovatik.com.au <svg width="11" height="11" viewBox="0 0 12 12" aria-hidden="true"><g fill="none" stroke="#fff" stroke-width="1.2"><rect x="1" y="2.5" width="10" height="7"/><path d="M1 2.5l5 4 5-4"/></g></svg></div>
    <div class="contact__row">14 Marlow Street, Kelmscott WA 6111 <svg width="11" height="11" viewBox="0 0 12 12" aria-hidden="true"><path d="M6 11.5S2 7 2 4.5a4 4 0 0 1 8 0C10 7 6 11.5 6 11.5z" fill="#fff"/><circle cx="6" cy="4.5" r="1.4" fill="var(--sky)"/></svg></div>
    <div class="contact__row"><b>www.brovatik.com.au</b> <svg width="11" height="11" viewBox="0 0 12 12" aria-hidden="true"><g fill="none" stroke="#fff" stroke-width="1"><circle cx="6" cy="6" r="5"/><ellipse cx="6" cy="6" rx="2" ry="5"/><path d="M1 6h10"/></g></svg></div>
  </div>
  <div class="abs contact-tab">CONTACT US:</div>
</section>

</body>
</html>
```